Vela Errands Web Design Project

Homepage components
o Logo
o Rotating header
o Main menu
o Animation video
o Banners
o Members login
o Latest news

The design’s preferred colors are black (background), silver (main tabs) and white (text)

Site map:
• Home
• News
• About us
o Welcome Note
o Company Profile
• Member Log in
o Registered homepage
? Request a service (form)
? Services directory
? Update profile
? Services history
• Member registration
o Registration form
• Partners
Footer Menu
• Contact us
• Terms & Conditions
• Privacy policy
• Social media links
• Sitemap

Brief about the company:
Vela Errands is a Jordanian company dedicated to elevate and redefine the level of service in the country. We are set out to give premium services at affordable prices. In this fast paced environment that we live in, we barely have the luxury of free time anymore and we, at Vela Errands will be giving you that extra hour or two per day to spend as your heart desires!
By becoming a member you will get access to a world of comfort and peace of mind. We have done the homework on your behalf and have established the network of connections that will enable you to live a headache free life.
We will be providing our members with support and assistance in their day to day lives in the fields that consumes and wastes time the most. We are value driven and below is our “ever-growing” list of services that we will provide at excellent prices:
• Maintenance (carpentry, plumbing, electrical, painting, decorating, gardening… etc)
• Cleaning (pre and post tenancy, periodical deep cleaning, packing and moving services, laundry… etc)
• Personalized delivery services (grocery, important documents, office related supplies, posting cheques, food, paying bills… etc)
• Passport, driving license and ID reissuance
• Travel arrangements (flights, hotels, airport transfers… etc)
• Premium car rental services
• Restaurant reservations
• IT assistance
• Event planning and all related services
• Catering arrangements

Aside from all the services we have on offer we have collaborated with a number of places (that we like to call partners) in town where Vela Errands members are entitled to benefits and privileges that will most certainly add value to their membership. Alongside our partners we have come up with the best formula that will please our members. Below are some of our current partners:

Requirements
Must have
• Homepage components
o Logo
o Rotating header
o Main menu
o Animation video
o Banners
o Members login
o Latest news

```html
<!DOCTYPE html>
<html lang="en">
<head>
<meta charset="utf-8">
<title>Vela Errands — We make life easier</title>
<link rel="stylesheet" href="https://fonts.googleapis.com/css2?family=Ubuntu:wght@400;500&family=Yanone+Kaffeesatz:wght@400&family=Lato:wght@400&family=Patrick+Hand&display=swap">
<style>
:root{
  --page:#2a2526;
  --strip:#6b6768;
  --silver-top:#c9c7c8;
  --silver-bottom:#a9a7a8;
  --nav-top:#2b2829;
  --nav-bottom:#0d0b0c;
  --panel:#1b1819;
  --footer:#151213;
  --tab:#3c3a37;
  --ink:#ffffff;
  --soft-ink:#e2e2e2;
  --link:#8b8d5c;
  --field:#222;
  --button:#4a4546;
}
*{margin:0;padding:0;box-sizing:border-box}
html,body{width:1200px;height:1158px;overflow:hidden}
body{background:var(--page);font-family:"Ubuntu",sans-serif;color:var(--ink);position:relative}
.abs{position:absolute}
.top-strip{left:0;top:0;width:1200px;height:9px;background:var(--strip)}

.header{left:20px;top:51px;width:1160px;height:131px;border-radius:10px 10px 0 0;
  background:linear-gradient(180deg,var(--silver-top),var(--silver-bottom))}
.brand{left:36px;top:20px;font-family:"Ubuntu",sans-serif;font-weight:400;font-size:48px;color:#1e1c1d;letter-spacing:1px}
.tagline{left:78px;top:73px;font-size:19px;color:#fff;letter-spacing:.5px}
.search{left:826px;top:46px;width:246px;height:35px;border-radius:8px;background:#e3e7e5;
  font-size:14px;color:#9a9d9c;padding:9px 18px;letter-spacing:1px}
.search-icon{left:1080px;top:43px}

.nav{left:0;top:182px;width:1200px;height:41px;background:linear-gradient(180deg,var(--nav-top),var(--nav-bottom))}
.nav ul{list-style:none;display:flex;height:100%}
.nav li{font-size:15px;color:var(--soft-ink);letter-spacing:1px;line-height:18px;padding-top:10px;height:100%}
.nav .sep{position:absolute;top:3px;width:1px;height:33px;background:#8a8687}
.new-account{left:1005px;top:189px;width:175px;height:30px;border-radius:6px;
  background:linear-gradient(180deg,#5b5758,#343132);font-size:14px;letter-spacing:.8px;padding:7px 0 0 68px}
.new-account svg{position:absolute;left:18px;top:-11px}

.hero{left:98px;top:234px;width:992px;height:357px;border-radius:10px;overflow:hidden;
  background:linear-gradient(90deg,#0f0f0f 0%,#161616 45%,#5a5a5a 62%,#9a9a9a 78%,#c9c9c9 100%)}
.hero-title{left:138px;top:304px;font-family:"Yanone Kaffeesatz",sans-serif;font-size:37px;letter-spacing:.5px}
.hero-text{left:159px;top:367px;width:540px;font-size:14px;line-height:22px;letter-spacing:.6px;color:#e8e8e8}
.read-more{left:533px;top:453px;width:134px;height:39px;border-radius:8px;background:var(--button);
  font-size:12px;letter-spacing:1px;text-align:center;line-height:39px;color:#ddd}
.slider-dots{left:1090px;top:421px;width:37px;height:150px;background:#0c0a0b;border:1px solid #555;border-left:none}
.dot{position:absolute;left:5px;width:23px;height:23px;border-radius:50%;background:#f2f2f2}
.dot.active{background:#4e4c47}
.dot-arrow{left:1080px;top:473px}

.column{top:602px;width:288px;height:365px;border-radius:8px;background:var(--panel)}
.tab{height:38px;border-radius:8px;background:var(--tab);font-size:18px;letter-spacing:1px;text-align:center;line-height:36px}
.news-date{font-size:12px;letter-spacing:.5px;color:#ddd;text-align:right;width:100px}
.news-text{font-size:12px;line-height:19px;letter-spacing:.6px;width:260px}
.intro{left:346px;top:662px;width:258px;font-size:12px;line-height:19px;letter-spacing:.5px}
.ticks{list-style:none}
.ticks li{position:relative;font-size:13px;letter-spacing:.7px;height:25px;padding-left:17px;line-height:18px}
.ticks li::before{content:"";position:absolute;left:0;top:4px;border-left:7px solid #fff;border-top:5px solid transparent;border-bottom:5px solid transparent}

.login{left:928px;top:628px;width:248px;height:269px;border-radius:6px;background:#0a0a0a;border:1px solid #3a3a3a;overflow:hidden}
.login-head{left:0;top:0;width:100%;height:48px;background:linear-gradient(180deg,#3c3a3b,#121011);
  font-size:20px;letter-spacing:-.3px;padding:13px 0 0 36px}
.field{left:16px;width:216px;height:34px;border-radius:6px;background:var(--field);border:1px solid #333;
  font-size:16px;padding:6px 0 0 45px;color:#fff}
.field .icon{position:absolute;left:0;top:0;width:34px;height:32px;border-radius:6px 0 0 6px;background:#2e2e2e}
.remember{left:24px;top:181px;font-size:11px;color:#aaa;padding-left:26px;line-height:18px}
.remember svg{position:absolute;left:0;top:0}
.login-btn{left:152px;top:171px;width:80px;height:31px;border-radius:4px;background:linear-gradient(180deg,#2a2a2a,#121212);
  border:1px solid #3a3a3a;font-size:16px;text-align:center;line-height:29px}
.login-foot{left:0;top:225px;width:100%;height:44px;background:#1e1c1d;border-top:1px solid #333;display:flex}
.login-foot span{flex:1;font-size:11px;color:#aaa;padding:13px 0 0 16px;position:relative}
.login-foot span+span{border-left:1px solid #333}
.login-foot span::before{content:"";position:absolute;left:6px;top:17px;width:6px;height:6px;background:#ccc}

.footer{left:19px;top:938px;width:1159px;height:220px;background:var(--footer);border-radius:0 14px 0 0}
.foot-col h3{font-family:"Lato",sans-serif;font-weight:400;font-size:24px;margin-bottom:18px}
.foot-col ul{list-style:none}
.foot-col li{font-size:12px;color:var(--link);letter-spacing:.6px;height:25px;padding-left:13px;position:relative}
.foot-col li::before{content:"›";position:absolute;left:0;top:-3px;color:#ccc;font-size:12px}
.follow{left:967px;top:1018px;font-family:"Patrick Hand",cursive;font-size:30px;letter-spacing:2px}
.social{left:914px;top:1053px;width:232px;height:66px;border-radius:8px;background:#050505}
.social i{position:absolute;top:17px;width:33px;height:33px;border-radius:50%}
</style>
</head>
<body>
<div class="abs top-strip"></div>

<header class="abs header">
  <div class="abs brand">Vela Errands</div>
  <div class="abs tagline">We make life easier</div>
  <div class="abs search">Search</div>
  <svg class="abs search-icon" width="38" height="40" viewBox="0 0 38 40" aria-hidden="true">
    <circle cx="15" cy="15" r="11" fill="#dfe9f0" stroke="#8a9299" stroke-width="3"/>
    <line x1="23" y1="24" x2="34" y2="36" stroke="#4a4a4a" stroke-width="6" stroke-linecap="round"/>
  </svg>
</header>

<nav class="abs nav">
  <ul>
    <li class="abs" style="left:20px">Home</li>
    <li class="abs" style="left:104px">About us</li>
    <li class="abs" style="left:215px">Login</li>
    <li class="abs" style="left:293px">Partners</li>
    <li class="abs" style="left:399px">Contact us</li>
  </ul>
  <span class="sep" style="left:89px"></span>
  <span class="sep" style="left:190px"></span>
  <span class="sep" style="left:275px"></span>
  <span class="sep" style="left:381px"></span>
  <span class="sep" style="left:493px"></span>
</nav>
<div class="abs new-account">
  <svg width="40" height="40" viewBox="0 0 40 40" aria-hidden="true">
    <circle cx="14" cy="10" r="7" fill="#111"/><path d="M2 40 Q2 19 14 19 Q26 19 26 40Z" fill="#111"/>
    <circle cx="26" cy="13" r="6" fill="#e6e6e6"/><path d="M16 40 Q16 21 26 21 Q36 21 36 40Z" fill="#e6e6e6"/>
  </svg>
  New Account
</div>

<section class="abs hero" role="img" aria-label="Black and white photograph of two businessmen shaking hands"></section>
<h1 class="abs hero-title" style="font-weight:400">Vela Errands is a Jordanian company</h1>
<p class="abs hero-text">We are set out to give premium services at affordable prices. In this fast paced environment that we live in, we barely have the luxury of free time anymore and we, at Vela Errands will be giving you that extra hour or two per day to spend as your heart desires</p>
<div class="abs read-more">Read More</div>
<div class="abs slider-dots">
  <span class="dot" style="top:13px"></span>
  <span class="dot active" style="top:45px"></span>
  <span class="dot" style="top:75px"></span>
  <span class="dot" style="top:107px"></span>
</div>
<svg class="abs dot-arrow" width="8" height="10" aria-hidden="true"><path d="M0 0L7 5L0 10Z" fill="#fff"/></svg>

<section class="abs column" style="left:20px"></section>
<div class="abs tab" style="left:74px;top:604px;width:142px">Latest News</div>
<div class="abs news-date" style="left:192px;top:650px">10/10/12</div>
<p class="abs news-text" style="left:39px;top:670px">Lorem ipsum dolor sit amet, consectetuer adipiscing</p>
<div class="abs news-date" style="left:192px;top:718px">10/10/12</div>
<p class="abs news-text" style="left:40px;top:738px">Lorem ipsum dolor sit amet, consectetuer adipiscing</p>
<div class="abs news-date" style="left:194px;top:792px">10/10/12</div>
<p class="abs news-text" style="left:41px;top:812px">Lorem ipsum dolor sit amet, consectetuer adipiscing</p>
<div class="abs news-date" style="left:195px;top:873px">10/10/12</div>
<p class="abs news-text" style="left:42px;top:893px">Lorem ipsum dolor sit amet, consectetuer adipiscing</p>

<section class="abs column" style="left:322px"></section>
<div class="abs tab" style="left:381px;top:604px;width:173px">Why Choose Us?</div>
<p class="abs intro">Lorem ipsum dolor sit amet, consectetuer adipiscingLorem ipsum dolor sit amet, consectetuer adipiscingLorem ipsum dolor sit amet, consectetuer adipiscing</p>
<ul class="abs ticks" style="left:361px;top:774px">
  <li>Lorem ipsum dolor consectetuer</li>
  <li>Adipiscing elit, diam nonummy</li>
  <li>Nibh euismod tincidunt laoreet</li>
  <li>Dolore magna aliquam volutpat</li>
  <li>Ut wisi enim ad minim veniam</li>
</ul>

<section class="abs column" style="left:623px"></section>
<div class="abs tab" style="left:673px;top:601px;width:173px">Our Services</div>
<ul class="abs ticks" style="left:646px;top:665px">
  <li>Lorem ipsum dolor consectetuer</li>
  <li>Adipiscing elit, diam nonummy</li>
  <li>Nibh euismod tincidunt laoreet</li>
  <li>Dolore magna aliquam volutpat</li>
  <li>Ut wisi enim ad minim veniam</li>
</ul>
<ul class="abs ticks" style="left:646px;top:807px">
  <li>Lorem ipsum dolor consectetuer</li>
  <li>Adipiscing elit, diam nonummy</li>
  <li>Nibh euismod tincidunt laoreet</li>
  <li>Dolore magna aliquam volutpat</li>
  <li>Ut wisi enim ad minim veniam</li>
</ul>

<footer class="abs footer"></footer>

<aside class="abs login">
  <div class="abs login-head">Login Panel</div>
  <div class="abs field" style="top:79px"><span class="icon"><svg width="34" height="32" aria-hidden="true"><circle cx="17" cy="12" r="4" fill="#aaa"/><path d="M10 24Q10 17 17 17Q24 17 24 24Z" fill="#aaa"/></svg></span>Username</div>
  <div class="abs field" style="top:124px"><span class="icon"><svg width="34" height="32" aria-hidden="true"><path d="M13 15V12a4 4 0 0 1 8 0v3" fill="none" stroke="#aaa" stroke-width="2"/><rect x="11" y="15" width="12" height="9" rx="1" fill="#aaa"/></svg></span>Password</div>
  <div class="abs remember"><svg width="20" height="20" aria-hidden="true"><rect x="1" y="3" width="15" height="15" fill="#333"/><path d="M4 10L8 15L18 1" fill="none" stroke="#eee" stroke-width="3"/></svg>Remember Me</div>
  <div class="abs login-btn">Login</div>
  <div class="abs login-foot"><span>Forgot Password ?</span><span>New Account</span></div>
</aside>

<div class="abs foot-col" style="left:60px;top:1003px"><h3>About Us</h3><ul><li>Lorem ipsum dolo</li><li>Lorem ipsum dolo</li><li>Lorem ipsum dolo</li></ul></div>
<div class="abs foot-col" style="left:227px;top:1003px"><h3>Advice</h3><ul><li>Lorem ipsum dolo</li><li>Lorem ipsum dolo</li><li>Lorem ipsum dolo</li></ul></div>
<div class="abs foot-col" style="left:394px;top:1003px"><h3>Join In</h3><ul><li>Lorem ipsum dolo</li><li>Lorem ipsum dolo</li><li>Lorem ipsum dolo</li></ul></div>
<div class="abs foot-col" style="left:560px;top:1003px"><h3>Downloads</h3><ul><li>Lorem ipsum dolo</li><li>Lorem ipsum dolo</li><li>Lorem ipsum dolo</li></ul></div>

<div class="abs follow">Follow Us</div>
<div class="abs social" aria-label="Social media links">
  <i style="left:31px;background:#5aa9d6"></i>
  <i style="left:79px;background:#4a5d8f"></i>
  <i style="left:127px;background:#d9d9d9"></i>
  <i style="left:177px;background:#e6801f"></i>
</div>
</body>
</html>
```